Maple Home Health Care of San Diego needs a brochure to advertise its services.

We need a brochure for a new company called Maple Home Health Care of San Diego, Inc. We provide skilled home health care services such as skilled nursing, physical, occupational, and speech therapy, medical social work, and home health aide services. Our patient population is mostly 65 years and older. We market our services in the community, including hospitals, skilled nursing and assisted living facilities, doctor's offices etc. We would like to see designs that are easy to read, go with our logo color, which is green, and includes pictures of multicultural elderly individuals receiving medical or rehab care in or surrounding the home. Please include the information contained in the files attached, which has our services, about home health care, and our mission and vision.
Maple Home Health Care of San Diego, Inc.
4827 Harbor Crest Lane, Suite 5B
Encinitas, CA 92031
760-418-LEAF (office)
76- 529-LEAF (fax)
760-284-5370 (cell)

Target Market(s)

See above

Industry/Entity Type

Home Health Care

Font styles to use
Sans Serif

Colors
9bcb3c
add136

Requirements
Must have
• Must be tri-fold and geared toward an elderly and medical field population. Please view some other home health agency brochures out there for examples.

```html
<!DOCTYPE html>
<html lang="en">
<head>
<meta charset="utf-8">
<title>Maple Home Health Care of San Diego – Brochure Inside</title>
<link href="https://fonts.googleapis.com/css2?family=Arimo:wght@400;700&display=swap" rel="stylesheet">
<style>
  :root {
    --page-bg: #ececec;
    --paper: #ffffff;
    --leaf-green: #9bcb3c;
    --lime-green: #add136;
    --heading-green: #1f9a3f;
    --bullet-green: #3aa346;
    --subhead-red: #8e1b1b;
    --ink: #2a2a2a;
    --kitchen-light: #e9dfcf;
    --kitchen-warm: #b89a78;
    --sunset-deep: #6e1410;
    --sunset-mid: #b7321b;
    --sunset-glow: #f08a2a;
  }
  * { box-sizing: border-box; margin: 0; padding: 0; }
  html, body { width: 1200px; height: 1000px; overflow: hidden; }
  body {
    background: var(--page-bg);
    font-family: "Arimo", Arial, sans-serif;
    color: var(--ink);
    position: relative;
  }
  .brochure {
    position: absolute;
    left: 40px; top: 67px;
    width: 1120px; height: 866px;
    display: grid;
    grid-template-columns: repeat(3, 1fr);
    background: var(--paper);
    box-shadow: 0 10px 30px rgba(0,0,0,.18);
  }
  .panel { position: relative; overflow: hidden; }

  /* Panel 1 – vision */
  .vision {
    position: absolute; left: 0; top: 0; width: 100%; height: 390px;
    background: var(--lime-green);
    padding: 26px 26px 0 24px;
    clip-path: polygon(0 0, 100% 0, 100% 360px, 46% 360px, 40% 390px, 34% 360px, 0 360px);
    z-index: 2;
  }
  .vision h2 { color: #fff; font-size: 24px; font-weight: 700; margin-bottom: 12px; }
  .vision ul { list-style: none; }
  .vision li {
    color: var(--ink); font-size: 15.5px; line-height: 1.22;
    padding-left: 16px; position: relative; margin-bottom: 4px;
  }
  .vision li::before {
    content: ""; position: absolute; left: 0; top: 6px;
    width: 7px; height: 7px; border-radius: 50%; background: var(--bullet-green);
  }
  .photo-kitchen {
    position: absolute; left: 0; top: 330px; width: 100%; bottom: 0;
    background: linear-gradient(170deg, var(--kitchen-light) 0%, #d8c8b0 45%, var(--kitchen-warm) 100%);
  }
  .brand-mark {
    position: absolute; display: flex; align-items: center; gap: 12px;
    color: #fff; font-weight: 400; font-size: 17px; line-height: 1.2; letter-spacing: .5px;
  }
  .brand-mark .dot {
    width: 46px; height: 46px; border-radius: 50%; background: rgba(255,255,255,.35); flex: none;
  }
  .photo-kitchen .brand-mark { left: 40px; top: 70px; width: 300px; }

  /* Panels 2 & 3 – services */
  .services { padding: 42px 26px 0 28px; }
  .services h1 {
    color: var(--heading-green); font-size: 25px; font-weight: 700; line-height: 1.15;
    margin-bottom: 22px;
  }
  .service { margin-bottom: 16px; }
  .service h3 { color: var(--subhead-red); font-size: 15.5px; font-weight: 700; margin-bottom: 3px; }
  .service ul { list-style: none; }
  .service li {
    font-size: 15.5px; line-height: 1.22; padding-left: 16px; position: relative;
  }
  .service li::before {
    content: ""; position: absolute; left: 0; top: 6px;
    width: 7px; height: 7px; border-radius: 50%; background: var(--bullet-green);
  }
  .panel-three .services { padding-top: 36px; }
  .photo-sunset {
    position: absolute; left: 0; right: 0; bottom: 0; height: 420px;
    background: radial-gradient(circle at 78% 62%, var(--sunset-glow) 0%, var(--sunset-mid) 32%, var(--sunset-deep) 85%);
    clip-path: polygon(0 30px, 24% 30px, 30% 0, 36% 30px, 100% 30px, 100% 100%, 0 100%);
  }
  .photo-sunset .brand-mark { left: 36px; top: 110px; width: 300px; }
</style>
</head>
<body>
  <main class="brochure">
    <section class="panel panel-one">
      <div class="vision">
        <h2>Vision</h2>
        <ul>
          <li>To be the provider of choice for quality home health care services, recognized for enduring dedication to provide innovative, professional, and compassionate care to the community we serve.</li>
          <li>To be one of the leading employers for healthcare professionals by providing our staff with an inviting work environment, competitive compensation and knowledgeable, trustworthy management and direction.</li>
          <li>To satisfy our patients' needs and exceed their expectations by utilizing best practices and quality care standards.</li>
        </ul>
      </div>
      <div class="photo-kitchen" role="img" aria-label="Photo of a smiling senior couple preparing food together in a home kitchen">
        <div class="brand-mark"><span class="dot"></span><span>Maple Home Health Care of San Diego</span></div>
      </div>
    </section>

    <section class="panel panel-two">
      <div class="services">
        <h1>We provide the following services in the comfort of your home:</h1>
        <div class="service">
          <h3>Skilled Nursing</h3>
          <ul>
            <li>Assess for changes in medical condition</li>
            <li>Education regarding disease management</li>
            <li>Teach how to manage and administer mediation</li>
            <li>Perform medical procedures such as catheter insertion, wound care, ostomy care, lab work and injections</li>
          </ul>
        </div>
        <div class="service">
          <h3>Physical Therapy</h3>
          <ul>
            <li>Focus on exercises and activities to improve balance, strength, and endurance, to reduce the risk of falls</li>
            <li>Improve ability to ambulate and/or transfer</li>
            <li>Evaluate the need for and train in the use of devices such as walker, cane, wheelchair</li>
            <li>Instruct in home exercise program</li>
          </ul>
        </div>
        <div class="service">
          <h3>Occupational Therapy</h3>
          <ul>
            <li>Focus on the ability to perform activities of daily living such as bathing, dressing, and household tasks</li>
            <li>Evaluate the need for and train in the use of adaptive equipment to aid in performing activities of daily living</li>
            <li>Teach energy conservation techniques</li>
            <li>Instruct in home exercise program</li>
          </ul>
        </div>
      </div>
    </section>

    <section class="panel panel-three">
      <div class="services">
        <div class="service">
          <h3>Speech Therapy</h3>
          <ul>
            <li>Improve communication skills</li>
            <li>Focus on the ability to swallow safely</li>
            <li>Improve memory and cognition/thinking skills</li>
          </ul>
        </div>
        <div class="service">
          <h3>Medical Social Work</h3>
          <ul>
            <li>Provide referrals to community resources</li>
            <li>Provide short-term counseling for patients and caregivers</li>
            <li>Assist with living arrangements, financial concerns, and long-term planning</li>
            <li>Focus on overall social and emotional health</li>
          </ul>
        </div>
        <div class="service">
          <h3>Home Health Aide</h3>
          <ul>
            <li>Provided when you are receiving skilled nursing, physical, occupational, or speech therapy</li>
            <li>Help with personal care on a short-term basis, such as bathing, dressing, toileting, light meal prep</li>
          </ul>
        </div>
      </div>
      <div class="photo-sunset" role="img" aria-label="Photo of an elderly couple silhouetted by the sea at sunset with gulls flying">
        <div class="brand-mark"><span class="dot"></span><span>Maple Home Health Care of San Diego</span></div>
      </div>
    </section>
  </main>
</body>
</html>
```